RMT Electrical Business Card Design

Have a logo to use, just looking for design around this, would like green theme, would like symbols in place of phone, fax, email etc.

Business

Contact Information for Business Card

RMT Electrical, Simon Ashcroft, simon@rmtelectrical-example.com.au, www.rmtelectrical-example.com.au, mobile 0412 555 019, phone (07) 3555 0142, fax (07) 3555 0142, Friendbook and WorkLink
addresses

```html
<!DOCTYPE html>
<html lang="en">
<head>
<meta charset="utf-8">
<title>RMT Electrical Business Card</title>
<link rel="stylesheet" href="https://fonts.googleapis.com/css2?family=Questrial&family=Montserrat:wght@700&display=swap">
<style>
  :root {
    --bg: #e4e4e4;
    --card: #ffffff;
    --green: #4cb748;
    --ink: #1c1c1c;
    --grey: #8a8a8a;
    --mark: #6d6d6d;
  }
  * { box-sizing: border-box; margin: 0; padding: 0; }
  html, body { width: 1200px; height: 1000px; overflow: hidden; }
  body {
    background: var(--bg);
    font-family: "Questrial", "Century Gothic", sans-serif;
    position: relative;
  }
  .card {
    position: absolute;
    left: 280px;
    width: 640px;
    height: 366px;
    background: var(--card);
    box-shadow: 0 6px 18px rgba(0,0,0,0.18);
    overflow: hidden;
  }
  .card--front { top: 90px; }
  .card--back { top: 540px; }
  .band { position: absolute; left: 0; right: 0; background: var(--green); }
  .band--top { top: 0; height: 18px; }
  .band--bottom { bottom: 0; height: 46px; }

  .brand {
    position: absolute;
    display: flex;
    align-items: center;
    color: var(--ink);
    white-space: nowrap;
  }
  .brand__dot {
    border-radius: 50%;
    background: var(--mark);
    flex: none;
  }
  .card--front .brand {
    left: 50%; top: 150px;
    transform: translateX(-50%);
    font-size: 56px;
    gap: 16px;
  }
  .card--front .brand__dot { width: 50px; height: 50px; }

  .card--back .brand {
    left: 40px; top: 60px;
    font-size: 34px;
    gap: 10px;
  }
  .card--back .brand__dot { width: 32px; height: 32px; }

  .person { position: absolute; left: 44px; top: 128px; }
  .person__name {
    font-family: "Montserrat", "Century Gothic", sans-serif;
    font-weight: 700;
    font-size: 22px;
    color: var(--ink);
    margin-bottom: 8px;
  }
  .person__line { font-size: 13px; color: var(--grey); line-height: 18px; }
  .social { margin-top: 22px; list-style: none; }
  .social li {
    display: flex; align-items: center; gap: 6px;
    font-size: 13px; color: var(--grey); line-height: 22px;
  }
  .social__box { width: 13px; height: 13px; background: #3d6aa8; border-radius: 2px; }

  .contact {
    position: absolute;
    right: 40px; top: 150px;
    font-size: 13px;
    line-height: 18px;
  }
  .contact__row { display: grid; grid-template-columns: 52px auto; }
  .contact__label { color: var(--green); text-align: right; padding-right: 6px; }
  .contact__value { color: var(--grey); }
</style>
</head>
<body>
  <section class="card card--front" aria-label="Card front">
    <div class="band band--top"></div>
    <div class="brand">
      <span class="brand__dot"></span>
      <span class="brand__name">RMT Electrical</span>
    </div>
    <div class="band band--bottom"></div>
  </section>

  <section class="card card--back" aria-label="Card back">
    <div class="band band--top"></div>
    <div class="brand">
      <span class="brand__dot"></span>
      <span class="brand__name">RMT Electrical</span>
    </div>
    <div class="person">
      <p class="person__name">Simon Ashcroft</p>
      <p class="person__line">simon@rmtelectrical-example.com.au</p>
      <p class="person__line">www.rmtelectrical-example.com.au</p>
      <ul class="social">
        <li><span class="social__box"></span>Friendbook address</li>
        <li><span class="social__box"></span>WorkLink address</li>
      </ul>
    </div>
    <div class="contact">
      <div class="contact__row"><span class="contact__label">mobile</span><span class="contact__value">0412 555 019</span></div>
      <div class="contact__row"><span class="contact__label">phone</span><span class="contact__value">(07) 3555 0142</span></div>
      <div class="contact__row"><span class="contact__label">fax</span><span class="contact__value">(07) 3555 0142</span></div>
    </div>
    <div class="band band--bottom"></div>
  </section>
</body>
</html>
```